依頼詳細
■依頼詳細
モノトーンでシック・スタイリッシュに、トップページの情報はコンパクトに見せたいと思っております。

■ホームページに期待する効果
L既存顧客の満足度向上
L問い合わせ数の向上
L認知度の向上
L売上の向上

■ターゲット
・男女比|3:7
・30代メイン
・会社員、自営業、主婦、学生、子ども

■コンテンツ素材
Lロゴ
L写真データ>HPからも引用OK

■デザインのテイスト
シンプル、知性的、シック、クール

■希望デザインカラー
白、黒のモノトーン

■参考サイト
http://www.koro-nest.com/
→色使いが好き。構成は見にくい。

http://wendoru.co.jp/
→雰囲気好き、情報をコンパクトにまとめているのが良い

http://tobelk527.com/
→色使いが好き。構成は縦に長すぎる。

※好きな雑誌の雰囲気
velipa
MORANE
大人TALIA

■SNS関連
・インスタグラム
・ノタバインへのリンク
https://notavine.me/

■サイトマップ
①Home
②Menu
③Staff
④Salon
⑤Blog(一覧) (詳細)
⑥News(一覧) (詳細)
⑦Gallery(一覧)
⑧Recommend
⑨Access
⑩Guest Snap
⑪Recruit
⑫Product
⑬Contact
⑭Calendar
サイトURL
http://www.dem-kua-sorin.com/index
ページ数
1ページ
希望イメージ
シンプル 複雑
単色 カラフル
暗い 明るい
日常 高級
遊び心 厳粛
未来的 伝統的
女性的 男性的
希望する色
白黒
納品ファイル
• イラストレーター形式 (.ai)
• フォトショップ形式 (.psd)
• PNG形式 (.png)
補足説明
●写真・素材
1)内観・外観写真
枚数が多いため、以下のURLよりダウンロードをお願い致します。

http://kumobako.jp/download/7c2e9b1d05a8f3e44290b6d1c7a58e02fbd9c4a1
ダウンロードパスワード kzm3p415

2)その他素材
今回、ピクセラ「https://jp.pixelora.com/」というサイトにて 制作中の間定期契約を致しました。
デザインの際には、一度仮素材にて配置を頂き、ピクセラ以外の素材は無料の物をご使用頂きたいです。
たくさんのご提案ありがとうございます!

さらなる提案を見てみたいため募集期間延長致します。
宜しくお願い致します。
■ 選んだ理由

画像をうまく活用していただき、かっこいいデザインです。
大変気に入りました。

■ 提案者全員のお礼・コメント

こちらの意図を組んでいただいたデザイン、ありがとうございます!

```html
<!DOCTYPE html>
<html lang="ja">
<head>
<meta charset="utf-8">
<title>DEM KUA SORIN</title>
<link href="https://fonts.googleapis.com/css2?family=Oswald:wght@400;600&family=Noto+Sans+JP:wght@400;700&display=swap" rel="stylesheet">
<style>
:root{
  --ink:#0d0d0d;
  --paper:#ffffff;
  --night:#141414;
  --smoke:#2a2a2a;
  --mist:#8a8a8a;
  --rule:#cfcfcf;
}
*{margin:0;padding:0;box-sizing:border-box}
html,body{width:1200px;height:2388px;overflow:hidden}
body{background:var(--paper);color:var(--ink);font-family:"Noto Sans JP",sans-serif;position:relative}

/* hero */
.hero{position:absolute;left:0;top:0;width:1200px;height:800px;
  background:linear-gradient(90deg,#0e0e0e 0%,#1c1c1c 40%,#3a3430 62%,#1a1a1a 85%,#0c0c0c 100%)}
.hero-photo{position:absolute;inset:0}
.site-logo{position:absolute;left:22px;top:22px;color:var(--paper);font-family:"Oswald",sans-serif;font-weight:600;font-size:30px;letter-spacing:.06em}
.menu-toggle{position:absolute;right:22px;top:22px;width:44px;height:44px;background:var(--ink);display:flex;flex-direction:column;justify-content:center;align-items:center;gap:6px}
.menu-toggle span{width:20px;height:2px;background:var(--paper)}
.hero-title{position:absolute;left:0;right:0;top:300px;text-align:center;color:var(--paper);font-family:"Oswald",sans-serif;font-weight:600}
.hero-title .main{font-size:120px;line-height:1;letter-spacing:.08em;display:block}
.hero-title .sub{font-size:34px;line-height:1.1;letter-spacing:.1em;display:block;margin-top:10px}
.reserve-tab{position:absolute;left:0;top:320px;width:38px;height:200px;background:var(--paper);border-radius:0 6px 6px 0;display:flex;align-items:center;justify-content:center}
.reserve-tab span{writing-mode:vertical-rl;font-size:12px;font-weight:700;letter-spacing:.2em;color:var(--ink)}
.side-links{position:absolute;right:22px;top:330px;display:flex;flex-direction:column;align-items:center;gap:18px;color:var(--paper)}
.side-links span{writing-mode:vertical-rl;font-family:"Oswald",sans-serif;font-size:12px;letter-spacing:.2em}
.side-links i{width:10px;height:10px;border:1px solid var(--paper);display:block}

/* grid */
.tile{position:absolute;overflow:hidden;color:var(--paper)}
.tile-label{position:absolute;text-align:center;font-family:"Oswald",sans-serif;font-weight:600;letter-spacing:.04em}
.more{display:inline-block;font-family:"Oswald",sans-serif;font-size:12px;letter-spacing:.15em;border-bottom:1px solid currentColor;padding:0 4px 3px;margin-top:12px}
.tile-menu{left:0;top:800px;width:600px;height:600px;background:linear-gradient(160deg,#3a3a3a 0%,#1e1e1e 55%,#2c2c2c 100%)}
.tile-menu .tile-label{left:230px;top:260px;font-size:46px}
.tile-gallery{left:600px;top:800px;width:300px;height:300px;background:linear-gradient(150deg,#151515,#262626)}
.tile-gallery .tile-label{left:0;right:0;top:70px;font-size:42px;line-height:1.05}
.tile-portrait{left:900px;top:800px;width:300px;height:300px;background:linear-gradient(120deg,#d9d9d9 0%,#6f6f6f 40%,#1c1c1c 70%)}
.tile-man{left:600px;top:1100px;width:300px;height:300px;background:linear-gradient(160deg,#2a2a2a,#4b4844 55%,#1a1a1a)}
.tile-staff{left:900px;top:1100px;width:300px;height:300px;background:linear-gradient(180deg,#4a4a48,#2a2a28)}
.tile-staff .tile-label{left:0;right:0;top:115px;font-size:46px}

/* news */
.news{position:absolute;left:0;top:1400px;width:1200px;height:400px;background:var(--paper)}
.news-col{position:absolute;top:70px;width:370px}
.news-col.info{left:200px}
.news-col.blog{left:630px}
.news-head{display:flex;justify-content:space-between;align-items:flex-end;border-bottom:3px solid var(--ink);padding-bottom:6px}
.news-head h2{font-family:"Oswald",sans-serif;font-weight:600;font-size:38px;line-height:1;letter-spacing:.03em}
.news-head .pill{background:var(--ink);color:var(--paper);font-family:"Oswald",sans-serif;font-size:9px;letter-spacing:.15em;padding:3px 10px;border-radius:10px;margin-bottom:4px}
.news-list{list-style:none}
.news-list li{border-bottom:1px solid var(--rule);padding:12px 0 10px}
.news-list time{font-family:"Oswald",sans-serif;font-size:11px;color:var(--mist);display:block}
.news-list p{font-size:12px;line-height:1.6;margin-top:2px}

/* salon */
.salon{position:absolute;left:0;top:1800px;width:1200px;height:532px;color:var(--paper);text-align:center;
  background:linear-gradient(90deg,#0c0c0c 0%,#1e1e1e 30%,#3a3a3a 50%,#1e1e1e 70%,#0c0c0c 100%)}
.salon-photo{position:absolute;inset:0}
.salon-body{position:absolute;left:0;right:0;top:60px}
.salon h2{font-family:"Oswald",sans-serif;font-weight:600;font-size:44px;letter-spacing:.04em;margin-bottom:12px}
.salon h3{font-family:"Oswald",sans-serif;font-weight:600;font-size:16px;letter-spacing:.12em;margin-top:18px}
.salon p{font-size:13px;line-height:1.7;margin-top:4px}
.salon .more{margin-top:26px}

/* footer */
.site-footer{position:absolute;left:0;top:2332px;width:1200px;height:56px;background:var(--ink);color:var(--mist);font-family:"Oswald",sans-serif;font-size:11px;letter-spacing:.1em;text-align:center;line-height:56px}
.to-top{position:absolute;right:22px;top:2300px;width:40px;height:40px;background:var(--ink);border:1px solid var(--smoke);display:flex;align-items:center;justify-content:center}
</style>
</head>
<body>

<header class="hero">
  <div class="hero-photo" role="img" aria-label="Dark moody portrait of a woman with long hair resting her chin on her hand, set in a salon interior"></div>
  <div class="site-logo">DEM KUA SORIN</div>
  <div class="menu-toggle" aria-label="Menu"><span></span><span></span><span></span></div>
  <div class="reserve-tab"><span>WEB予約</span></div>
  <h1 class="hero-title"><span class="main">DEM</span><span class="sub">KUA SORIN</span></h1>
  <nav class="side-links"><i></i><span>SNAPFEED</span><i></i><span>NOTAVINE</span></nav>
</header>

<section>
  <a class="tile tile-menu" role="img" aria-label="Woman in sunglasses seated on a dark sofa">
    <div class="tile-label">MENU<br><span class="more">MORE</span></div>
  </a>
  <a class="tile tile-gallery">
    <div class="tile-label">STYLE<br>GALLERY<br><span class="more">MORE</span></div>
  </a>
  <div class="tile tile-portrait" role="img" aria-label="Side profile portrait of a woman by a bright window"></div>
  <div class="tile tile-man" role="img" aria-label="Man in a white t-shirt seated in a dim room"></div>
  <a class="tile tile-staff" role="img" aria-label="Salon staff photo in warm dark tones">
    <div class="tile-label">STAFF<br><span class="more">MORE</span></div>
  </a>
</section>

<section class="news">
  <div class="news-col info">
    <div class="news-head"><h2>INFORMATION</h2><span class="pill">MORE</span></div>
    <ul class="news-list">
      <li><time>2017.10.24</time><p>年末年始の営業時間についてお知らせいたします。</p></li>
      <li><time>2017.10.16</time><p>新メニューのカラーケアを始めました。</p></li>
      <li><time>2017.10.02</time><p>スタッフ募集のご案内を更新しました。</p></li>
    </ul>
  </div>
  <div class="news-col blog">
    <div class="news-head"><h2>BLOG</h2><span class="pill">MORE</span></div>
    <ul class="news-list">
      <li><time>2017.10.22</time><p>秋におすすめの落ち着いたカラーをご紹介します。</p></li>
      <li><time>2017.10.12</time><p>自宅でできる簡単なスタイリングのコツ。</p></li>
      <li><time>2017.10.05</time><p>新しいトリートメントを試してみました。</p></li>
    </ul>
  </div>
</section>

<section class="salon">
  <div class="salon-photo" role="img" aria-label="Silhouette of a woman standing in a softly lit salon interior"></div>
  <div class="salon-body">
    <h2>SALON INFO</h2>
    <h3>ADDRESS</h3>
    <p>大阪府大阪市北区架空町1-2-3 白黒ビル2F</p>
    <h3>TELL</h3>
    <p>06-0000-1234</p>
    <h3>OPEN</h3>
    <p>平日 OPEN 10:00 / CLOSE 20:00<br>土日祝 OPEN 9:00 / CLOSE 19:00</p>
    <h3>CLOSE</h3>
    <p>毎週火曜日・第1、第3月曜日</p>
    <span class="more">MORE</span>
  </div>
</section>

<a class="to-top" aria-label="Back to top">
  <svg width="14" height="10" viewBox="0 0 14 10"><path d="M1 9 L7 2 L13 9" fill="none" stroke="#fff" stroke-width="1.5"/></svg>
</a>
<footer class="site-footer">Copyright 2017 DEM KUA SORIN All Rights Reserved.</footer>

</body>
</html>
```